Business Card Design Project

We have recently completed CraftHive projects for a new logo and wesbite.
We now require new business cards.
We hand out very little printed material to clients as all information is online. When we do hand out something, like a business card, we want it to have real impact and make a statement about the quality and professionalism of our company.
We have an idea of what we want our card to look like but we want a designer to make sure they have impact and look great.
Our requirements are…
Size: 85mm X 55mm - Landscape
Front of card: Logo plus the following contact information.
Tobias Marsh
Operations Manager
Phone +44(0) 1632 xxx xxx
Mobile +44(0) 7700 xxx xxx
Email tobym@korvexsys.example
Address 19 Pellow Row, Aberdeen AB12 3QJ
Website www.korvexsys.example
How you layout the front of the card is up to you, we would like to see some different ideas. Attached are two versions of our logo that may be used.
Back of card: We would like this to be simple but again have impact. Our current thought is to have the logo or just the large W design from the logo in white against a dark background, perhaps made up from the dark green in the logo.
The logos are attached so you can see the colours in them but the dark ones are..
Dark Blue = C:88, M:55, Y:44, K:28
Dark Green = C:87, M:53, Y:50, K:50
We sometimes also use a bright orange as an accent or highlight colour…
Orange: = C:0, M:39, Y:94, K:0

```html
<!DOCTYPE html>
<html lang="en">
<head>
<meta charset="utf-8">
<title>Korvex Systems — Business Card Set</title>
<link rel="stylesheet" href="https://fonts.googleapis.com/css2?family=Source+Sans+3:wght@400;600;700&display=swap">
<style>
  :root {
    --ink-dark: #22444b;
    --ink-deep: #1f4049;
    --moss: #7f9660;
    --teal-light: #72aab3;
    --paper: #ffffff;
    --stage: #e6e3de;
    --text: #2c3a3e;
    --card-shadow: 0 3px 8px rgba(0,0,0,0.25);
  }
  * { box-sizing: border-box; margin: 0; padding: 0; }
  html, body {
    width: 1200px; height: 800px; overflow: hidden;
    background: var(--stage);
    font-family: "Source Sans 3", "Myriad Pro", Arial, sans-serif;
  }
  .canvas { position: relative; width: 1200px; height: 800px; }
  .card {
    position: absolute; width: 502px; height: 324px;
    box-shadow: var(--card-shadow); overflow: hidden;
  }
  .card--front { left: 81px; top: 65px; background: var(--paper); }
  .card--back-dark { left: 609px; top: 67px; background: var(--ink-deep); }
  .card--back-gradient {
    left: 85px; top: 407px;
    background: linear-gradient(150deg, var(--ink-dark) 0%, #4f6d55 50%, var(--moss) 85%);
  }
  .card--back-light { left: 610px; top: 407px; background: var(--paper); }

  /* front */
  .edge-bar { position: absolute; left: 0; width: 11px; }
  .edge-bar--top { top: 0; height: 148px; background: var(--ink-dark); }
  .edge-bar--bottom { top: 155px; bottom: 0; background: var(--teal-light); }
  .brand {
    position: absolute; left: 48px; top: 62px;
    color: var(--ink-dark); font-weight: 700; font-size: 34px; letter-spacing: 1px;
    display: flex; align-items: center; gap: 12px; line-height: 1;
  }
  .brand__dot { width: 22px; height: 22px; border-radius: 50%; background: var(--ink-dark); }
  .contact-person { position: absolute; right: 22px; top: 160px; text-align: right; }
  .contact-person__name { color: var(--ink-dark); font-weight: 700; font-size: 19px; letter-spacing: 0.3px; }
  .contact-person__role { color: var(--text); font-size: 14px; margin-top: 2px; }
  .contact-list {
    position: absolute; right: 22px; top: 224px; list-style: none;
    font-size: 13px; color: var(--text); text-align: right;
  }
  .contact-list li { display: flex; justify-content: flex-end; align-items: center; gap: 6px; height: 18.5px; }
  .contact-list svg { width: 11px; height: 11px; fill: var(--ink-dark); }
  .address { position: absolute; left: 47px; top: 282px; font-size: 13px; color: var(--text); }

  /* backs */
  .back-mark {
    position: absolute; left: 0; right: 0; top: 95px; text-align: center;
    font-weight: 700; font-size: 54px; letter-spacing: 3px; line-height: 1;
  }
  .back-mark small { display: block; font-size: 18px; font-weight: 600; letter-spacing: 8px; margin-top: 10px; }
  .back-url {
    position: absolute; left: 0; right: 0; text-align: center;
    font-size: 16px; letter-spacing: 3px;
  }
  .card--back-dark .back-mark, .card--back-dark .back-url,
  .card--back-gradient .back-mark, .card--back-gradient .back-url { color: var(--paper); }
  .card--back-light .back-mark, .card--back-light .back-url { color: var(--ink-dark); }
  .card--back-dark .back-url { top: 268px; }
  .card--back-gradient .back-url, .card--back-light .back-url { top: 267px; }
</style>
</head>
<body>
<main class="canvas">

  <section class="card card--front" aria-label="Card front">
    <div class="edge-bar edge-bar--top"></div>
    <div class="edge-bar edge-bar--bottom"></div>
    <div class="brand"><span class="brand__dot"></span>KORVEX SYSTEMS</div>
    <div class="contact-person">
      <div class="contact-person__name">TOBIAS MARSH</div>
      <div class="contact-person__role">Operations Manager</div>
    </div>
    <ul class="contact-list">
      <li>+44(0) 1632 xxx xxx
        <svg viewBox="0 0 12 12"><circle cx="6" cy="6" r="5.5" fill="none" stroke="#22444b"/><path d="M3.8 3.2l1.2-.4.7 1.5-.7.6c.3.8.9 1.4 1.6 1.7l.6-.7 1.5.7-.4 1.2c-2.5 0-4.6-2.1-4.5-4.6z"/></svg></li>
      <li>+44(0) 7700 xxx xxx
        <svg viewBox="0 0 12 12"><rect x="3.5" y="0.5" width="5" height="11" rx="1"/><rect x="4.3" y="1.8" width="3.4" height="6.5" fill="#fff"/></svg></li>
      <li>tobym@korvexsys.example
        <svg viewBox="0 0 12 12"><rect x="0.5" y="2.5" width="11" height="7.5"/><path d="M0.8 2.8L6 7l5.2-4.2" fill="none" stroke="#fff" stroke-width="0.9"/></svg></li>
      <li>www.korvexsys.example
        <svg viewBox="0 0 12 12"><circle cx="6" cy="6" r="5.5"/><path d="M0.5 6h11M6 0.5v11M6 0.5c-3 3-3 8 0 11M6 0.5c3 3 3 8 0 11" fill="none" stroke="#fff" stroke-width="0.7"/></svg></li>
    </ul>
    <div class="address">19 Pellow Row, Aberdeen AB12 3QJ</div>
  </section>

  <section class="card card--back-dark" aria-label="Card back, dark">
    <div class="back-mark">KORVEX<small>SYSTEMS</small></div>
    <div class="back-url">www.korvexsys.example</div>
  </section>

  <section class="card card--back-gradient" aria-label="Card back, gradient">
    <div class="back-mark">KORVEX<small>SYSTEMS</small></div>
    <div class="back-url">www.korvexsys.example</div>
  </section>

  <section class="card card--back-light" aria-label="Card back, light">
    <div class="back-mark">KORVEX<small>SYSTEMS</small></div>
    <div class="back-url">www.korvexsys.example</div>
  </section>

</main>
</body>
</html>
```